Business Card Design

We are state certified residental contractors who specialize in insurance claims. We are insurance restoration experts and have a state multi-lines insurance adjusters license #W581403. We produce insurance grade estimates using the most widely used software in the industry. Our goal is to work for our customers! not the insurance company. Our edge is we don't take short cuts to please the adjuster/insurance company to insure future claims from them. We are experts at restoring damaged properties.from wind, water ,fire and smoke. We pride ourselfs on evaluating damages properly and providing extremely detailed estimates for restoration.We are also educated and experienced in identifiying and correcting indoor air quality issues as a result of common perils and defective materials. .We are not a franchise and are family owned and operated. We provide quality work using only the best local tradesman. We ourselfs are local tradesmen and helped build and restore our community over the past 30 years. We know first hand how our homes were built and are aware of many of the common problems that exist and how to address them. We are licensed insured and bonded.
Industry/Entity Type
Business
Contact Information for Business Card
Harbor Keystone LLC
Martin Calloway
4175 Pelican Rd unit K
Melbourne Fl.32815 Manager/State Certified Residental Contractor license# CRC1846052
321-555-0174 Office
321-555-0188 Fax

```html
<!DOCTYPE html>
<html lang="en">
<head>
<meta charset="utf-8">
<title>Harbor Keystone LLC – Business Card</title>
<link href="https://fonts.googleapis.com/css2?family=PT+Sans+Narrow:wght@700&family=Ubuntu:wght@400;500;700&display=swap" rel="stylesheet">
<style>
  :root {
    --backdrop: #5e0a0e;
    --card: #f6f6f6;
    --brand-red: #c8102e;
    --strip-grey: #ebebeb;
    --ink: #111111;
    --text-grey: #5a5a5a;
    --white: #ffffff;
  }
  * { margin: 0; padding: 0; box-sizing: border-box; }
  html, body { width: 1200px; height: 970px; overflow: hidden; }
  body {
    position: relative;
    background: var(--backdrop);
    font-family: "Ubuntu", Arial, sans-serif;
  }
  .card {
    position: absolute;
    width: 451px;
    height: 751px;
    background: var(--card);
    overflow: hidden;
    box-shadow: 0 10px 40px rgba(0,0,0,0.55);
  }
  .card--front { left: 88px; top: 142px; }
  .card--back { left: 632px; top: 146px; }

  /* Front */
  .front-mark {
    position: absolute;
    left: 208px; top: 210px;
    width: 36px; height: 36px;
    background: var(--brand-red);
  }
  .front-band {
    position: absolute;
    left: 50px; top: 320px;
    width: 401px; height: 77px;
    background: var(--brand-red);
    display: flex; align-items: center;
    padding-left: 10px;
  }
  .front-band__name {
    color: var(--white);
    font-weight: 700;
    font-size: 33px;
    letter-spacing: -0.3px;
  }
  .front-strip {
    position: absolute;
    left: 0; top: 377px;
    width: 401px; height: 76px;
    background: var(--strip-grey);
  }
  .license-line {
    position: absolute;
    font-size: 19px;
    color: var(--text-grey);
    white-space: nowrap;
  }
  .license-line__label { color: var(--brand-red); }
  .card--front .license-line { left: 55px; top: 416px; }

  /* Back */
  .side-bar {
    position: absolute;
    left: 0;
    width: 50px;
    background: repeating-linear-gradient(135deg, #c8102e 0 3px, #b50d28 3px 5px);
  }
  .side-bar--top { top: 0; height: 436px; }
  .side-bar--bottom { top: 641px; height: 110px; }
  .name-band {
    position: absolute;
    left: 116px; top: 114px;
    width: 307px; height: 51px;
    background: var(--brand-red);
    display: flex; align-items: center;
    padding-left: 33px;
  }
  .name-band__name {
    font-family: "PT Sans Narrow", "Arial Narrow", sans-serif;
    font-weight: 700;
    font-size: 37px;
    color: var(--white);
  }
  .job-title {
    position: absolute;
    left: 119px; top: 171px;
    font-size: 13px;
    color: var(--text-grey);
  }
  .back-company {
    position: absolute;
    left: 58px; top: 321px;
    font-weight: 700;
    font-size: 25px;
    color: var(--ink);
  }
  .card--back .license-line { left: 60px; top: 362px; font-size: 16px; }
  .contact-row {
    position: absolute;
    left: 0;
    width: 401px; height: 46px;
    background: var(--strip-grey);
    display: flex; align-items: center;
    font-size: 21px;
    color: var(--text-grey);
  }
  .contact-row__icon {
    width: 16px; height: 16px;
    margin-left: 61px; margin-right: 21px;
    flex: none;
  }
  .contact-row--continued { padding-left: 98px; }
  .row-1 { top: 436px; }
  .row-2 { top: 489px; }
  .row-3 { top: 542px; }
  .row-4 { top: 596px; }
</style>
</head>
<body>
  <section class="card card--front">
    <div class="front-mark"></div>
    <div class="front-strip"></div>
    <div class="front-band"><span class="front-band__name">Harbor Keystone LLC</span></div>
    <p class="license-line"><span class="license-line__label">license#</span> CRC1846052 321-555-0174</p>
  </section>

  <section class="card card--back">
    <div class="side-bar side-bar--top"></div>
    <div class="side-bar side-bar--bottom"></div>
    <div class="name-band"><span class="name-band__name">Martin Calloway</span></div>
    <p class="job-title">Manager/State Certified Residental Contractor</p>
    <p class="back-company">Harbor Keystone LLC</p>
    <p class="license-line"><span class="license-line__label">license#</span> CRC1846052 321-555-0174</p>

    <div class="contact-row row-1">
      <svg class="contact-row__icon" viewBox="0 0 16 16" aria-hidden="true">
        <path d="M8 1a5 5 0 0 0-5 5c0 3.5 5 9 5 9s5-5.5 5-9a5 5 0 0 0-5-5z" fill="none" stroke="#c8102e" stroke-width="2.2"/>
        <circle cx="8" cy="6" r="1.6" fill="#c8102e"/>
      </svg>
      <span>4175 Pelican Rd unit K,</span>
    </div>
    <div class="contact-row row-2 contact-row--continued"><span>Melbourne, Fl.32815</span></div>
    <div class="contact-row row-3">
      <svg class="contact-row__icon" viewBox="0 0 16 16" aria-hidden="true">
        <path d="M6 2h3v3H7.5v6H9v3H6c-1.2-2-1.6-4-1.6-6S4.8 4 6 2z" fill="#c8102e"/>
      </svg>
      <span>321-555-0188</span>
    </div>
    <div class="contact-row row-4">
      <svg class="contact-row__icon" viewBox="0 0 16 16" aria-hidden="true">
        <rect x="4" y="1.5" width="8" height="5" fill="none" stroke="#c8102e" stroke-width="1.2"/>
        <rect x="1.5" y="6.5" width="13" height="7.5" fill="none" stroke="#c8102e" stroke-width="1.2"/>
        <rect x="4" y="9" width="8" height="2" fill="#c8102e"/>
      </svg>
    </div>
  </section>
</body>
</html>
```